Delivery Docket urgent plus require many other designs for more stationary after this.

We need a new delivery docket design urgently as the one we have needs updating and we have changed our company name. Please do not copy the one I have uploaded as we do not feel this looks professional enough. I uploaded it as a few designers requested to see what we are currently using thank you.
It is quite complex in that we need a range of information to be on the one docket.
We are a Transport Company based in Australia that has a wide variety of items that we deliver such as water, sand and gravels and heavy equipment transport.
We would prefer to keep this design to A5 size as we will get them made into books. We are looking for a modern professional look. Although it is only a delivery docket this is given to all our customers so needs to look impressive.

We need our new logo on the docket (PRW). There will also need to be areas for our address and contact numbers, email etc these will be supplied to the winning designer to make the final adjustments so for now just put something generic in these spaces.
Needs to have an area for customer details, purchase order number, date and docket number (docket number to be in red)
Needs a section where we can list the type of product / and or service that has been provided and the amount / qty usually 3 lines will be enough for this. Need area under this where the customer can sign name and print name to say that the goods / and or services have been received.

Also required somewhere on the docket are the words, Tax Invoice will be issued based on the information provided on this docket. Conditions on back of page

We then need a separate section on the same page which we will use internally that the staff member can tear off and hand into the office. On this section it needs to have area where the driver can list km at start of job and at end with space to calculate km travelled, details of fuel purchased eg amount and litres, vehicle that is being used. also need to log down wheel bearing temps.
prime mover needs spaces as follows
Steer axel FL____________ Steer axel FR _________ 1st drive axel L_______
1st drive axel R_________ 2nd drive axel L_______ 2nd drive axel R________

For the trailers need something similar x 2 as have 2 trailers
1st axel DS_________ 1st axel PS_________ 2nd axel DS__________
2nd axel PS_________ 3rd axel DS_________ 3rd axel PS__________

I have included a few examples of designs we have used in past and ones that we like so you can get an idea of the colours we prefer, I have included some of the designs we are currently receiving for our logo that I like so you can get idea again of colours we prefer. There is much more we need designed also such as time sheets, more delivery dockets and letter heads so there is a lot of more work available to the winning designer.

Thank you

Target Market(s)

Customers

Font styles to use
Serif
Sans Serif

Colors

Designer to choose colors to be used in the design.

Requirements
Should not have
• Please don't copy old docket as we do not like it and nned new info on new design thank you

```html
<!DOCTYPE html>
<html lang="en">
<head>
<meta charset="utf-8">
<title>PRW Delivery Docket</title>
<link href="https://fonts.googleapis.com/css2?family=Montserrat:wght@500;600;700&family=Roboto:ital,wght@0,400;0,500;1,400&display=swap" rel="stylesheet">
<style>
:root{
  --ink:#1d1d1d;
  --black:#000;
  --red:#e3101a;
  --band:#666666;
  --panel:#f5f5f5;
  --panel-cool:#eef0ef;
  --rule:#3a3a3a;
  --muted:#555;
  --paper:#fff;
}
*{box-sizing:border-box;margin:0;padding:0}
html,body{width:1200px;height:930px;overflow:hidden;background:var(--paper)}
body{position:relative;font-family:"Roboto",Arial,sans-serif;color:var(--ink)}
.abs{position:absolute}
.heading{font-family:"Montserrat",Arial,sans-serif;font-weight:600;letter-spacing:.06em;text-transform:uppercase}

/* brand */
.brand{left:31px;top:35px;width:121px;height:95px;display:flex;align-items:center;justify-content:center;gap:8px}
.brand-mark{width:14px;height:14px;background:var(--ink)}
.brand-name{font-family:"Montserrat",sans-serif;font-weight:700;font-size:40px;color:var(--ink);letter-spacing:.04em}

/* contacts */
.contact{top:42px;width:190px;text-align:center;font-size:13px;line-height:20px;color:#333}
.contact svg{display:block;margin:0 auto 18px}
.divider{top:53px;width:1px;height:46px;background:#bbb}

/* docket header */
.docket-bar{left:694px;top:45px;width:486px;height:37px;display:flex}
.docket-no{background:var(--red);color:#fff;flex:0 0 310px;clip-path:polygon(0 0,100% 0,93% 100%,0 100%);display:flex;align-items:center;padding-left:12px;font-size:15px}
.docket-date{background:var(--black);color:#fff;flex:1;margin-left:-23px;display:flex;align-items:center;padding-left:44px;font-size:15px}
.customer-bar{left:694px;top:90px;width:486px;height:30px;background:var(--band);display:flex;align-items:center}
.customer-title{background:var(--black);color:#fff;height:100%;width:210px;clip-path:polygon(0 0,92% 0,100% 100%,0 100%);display:flex;align-items:center;padding-left:12px;font-size:13px}
.po{color:#fff;font-size:11px;margin-left:12px}
.customer-panel{left:694px;top:120px;width:486px;height:159px;background:var(--panel)}
.field{display:flex;align-items:flex-end;font-size:14px;font-weight:500;white-space:nowrap}
.field .line{flex:1;border-bottom:1px solid var(--rule);margin-left:5px;height:1px}
.customer-panel .field{position:absolute;left:12px;right:10px}

/* products */
.products{left:29px;top:294px;width:1151px}
.products-head{height:29px;background:var(--band);color:#fff;font-size:13px;display:flex;align-items:center}
.products-head .col-product{padding-left:60px;flex:1}
.products-head .col-qty{width:248px;text-align:center}
.products-row{height:33px;border-bottom:1px solid var(--rule);display:flex}
.products-row .col-product{flex:1;border-right:1px solid var(--rule)}
.products-row .col-qty{width:248px}
.products-note{height:52px;background:var(--panel);font-size:12px;font-style:italic;text-align:center;padding-top:18px}

/* receipt */
.receipt{left:29px;top:498px;width:1151px;height:68px;border:2px solid var(--black);display:flex}
.receipt .label{background:var(--black);color:#fff;font-size:15px;text-align:center;display:flex;align-items:center;justify-content:center;line-height:20px}
.receipt .space{flex:1}

.tear{left:0;top:601px;width:1200px;border-top:2px dashed var(--ink)}
.scissor{top:592px;width:22px;height:18px;background:var(--paper)}

/* office */
.office{left:29px;top:629px;width:1151px;height:271px;background:var(--panel)}
.office-title{top:16px;left:0;width:100%;display:flex;align-items:center;gap:14px;font-size:17px}
.office-title::before,.office-title::after{content:"";flex:1;border-top:1.5px solid var(--ink)}
.trip{top:72px;left:8px;right:11px;display:flex;gap:10px}
.trip .field{font-size:13px;font-weight:400}
.trip .value{border-bottom:1px solid var(--rule);font-size:10px;color:var(--muted);text-align:center;margin-left:4px;padding-bottom:2px}
.bearings{top:117px;left:0;width:100%;height:154px;background:var(--panel-cool)}
.bearings-title{top:20px;left:0;width:100%;display:flex;align-items:center;gap:10px;font-size:12px}
.bearings-title::before,.bearings-title::after{content:"";flex:1;border-top:1px solid var(--ink)}
.check{top:44px;display:flex;align-items:center;gap:8px;font-size:11px}
.box{width:17px;height:17px;border:2px solid var(--ink);position:relative}
.bearing{font-size:13px;font-weight:400;width:154px}
</style>
</head>
<body>

<div class="abs brand"><span class="brand-mark"></span><span class="brand-name">PRW</span></div>

<div class="abs contact" style="left:182px">
  <svg width="28" height="28" viewBox="0 0 28 28"><circle cx="14" cy="14" r="14" fill="#333"/><path d="M14 7a5 5 0 0 0-5 5c0 4 5 9 5 9s5-5 5-9a5 5 0 0 0-5-5zm0 7a2 2 0 1 1 0-4 2 2 0 0 1 0 4z" fill="#fff"/></svg>
  14 Harbour Way Ridgefield<br>Q 4310, Sydney, Australia
</div>
<div class="abs divider" style="left:383px"></div>
<div class="abs contact" style="left:349px">
  <svg width="28" height="28" viewBox="0 0 28 28"><circle cx="14" cy="14" r="14" fill="#333"/><path d="M10.5 8.5l2 2-1.2 1.6a8 8 0 0 0 4.6 4.6l1.6-1.2 2 2-1.5 1.8c-4.6-.5-8.6-4.5-9.1-9.1z" fill="#fff"/></svg>
  0400 555 0148<br>0400 555 0162
</div>
<div class="abs divider" style="left:521px"></div>
<div class="abs contact" style="left:488px">
  <svg width="28" height="28" viewBox="0 0 28 28"><circle cx="14" cy="14" r="14" fill="#333"/><g fill="none" stroke="#fff" stroke-width="1.3"><circle cx="14" cy="14" r="6"/><ellipse cx="14" cy="14" rx="2.6" ry="6"/><path d="M8 14h12M9 11h10M9 17h10"/></g></svg>
  info@prwtransport.com.au<br>www.prwtransport.com.au
</div>

<div class="abs docket-bar heading">
  <div class="docket-no">Delivery Docket No: 20512</div>
  <div class="docket-date">Date: __ / __ /____</div>
</div>
<div class="abs customer-bar heading">
  <div class="customer-title">Customer Details</div>
  <div class="po">Purchase Order No: 201234</div>
</div>
<div class="abs customer-panel">
  <div class="field" style="top:12px">Name<span class="line"></span></div>
  <div class="field" style="top:48px">Address<span class="line"></span></div>
  <div class="field" style="top:83px">City / State / Zip<span class="line"></span></div>
  <div class="field" style="top:119px">Phone<span class="line"></span><span style="margin-left:8px">Email</span><span class="line" style="margin-left:2px"></span></div>
</div>

<div class="abs products">
  <div class="products-head heading"><span class="col-product">Product / Services</span><span class="col-qty">Amount/ Qty</span></div>
  <div class="products-row"><span class="col-product"></span><span class="col-qty"></span></div>
  <div class="products-row"><span class="col-product"></span><span class="col-qty"></span></div>
  <div class="products-row"><span class="col-product"></span><span class="col-qty"></span></div>
  <div class="products-note">*** Tax Invoice will be issued based on the information provided on this docket. Conditions on back of page ***</div>
</div>

<div class="abs receipt heading">
  <div class="label" style="width:193px">Goods Received By<br>(Print Name)</div>
  <div class="space"></div>
  <div class="label" style="width:133px">Customer<br>Signature</div>
  <div class="space"></div>
  <div class="label" style="width:101px">Date of<br>Receiving</div>
  <div class="space" style="flex:0 0 107px"></div>
</div>

<div class="abs tear"></div>
<svg class="abs scissor" style="left:108px" viewBox="0 0 22 18"><g fill="none" stroke="#1d1d1d" stroke-width="1.8"><circle cx="5" cy="4" r="3"/><circle cx="5" cy="14" r="3"/><path d="M7.5 5.5L19 13M7.5 12.5L19 5"/></g></svg>
<svg class="abs scissor" style="left:432px" viewBox="0 0 22 18"><g fill="none" stroke="#1d1d1d" stroke-width="1.8"><circle cx="5" cy="4" r="3"/><circle cx="5" cy="14" r="3"/><path d="M7.5 5.5L19 13M7.5 12.5L19 5"/></g></svg>
<svg class="abs scissor" style="left:753px" viewBox="0 0 22 18"><g fill="none" stroke="#1d1d1d" stroke-width="1.8"><circle cx="5" cy="4" r="3"/><circle cx="5" cy="14" r="3"/><path d="M7.5 5.5L19 13M7.5 12.5L19 5"/></g></svg>
<svg class="abs scissor" style="left:1077px" viewBox="0 0 22 18"><g fill="none" stroke="#1d1d1d" stroke-width="1.8"><circle cx="5" cy="4" r="3"/><circle cx="5" cy="14" r="3"/><path d="M7.5 5.5L19 13M7.5 12.5L19 5"/></g></svg>

<section class="abs office">
  <div class="abs office-title heading">For Office Use Only</div>
  <div class="abs trip">
    <div class="field">Starting Point(km)<span class="value" style="width:52px">27450</span></div>
    <div class="field" style="margin-left:4px">Destination Point(km)<span class="value" style="width:56px;margin-left:12px">28190</span></div>
    <div class="field">Distance Travelled(km)<span class="value" style="width:44px;margin-left:12px">840</span></div>
    <div class="field" style="margin-left:36px">Fuel Used(Lt)<span class="value" style="width:52px">84</span></div>
    <div class="field" style="margin-left:8px">Amount($)<span class="value" style="width:52px">2560.00</span></div>
    <div class="field" style="flex:1;margin-left:6px">Vehhicle<span class="value" style="flex:1;text-align:left;padding-left:14px">Roadline 14 wheel</span></div>
  </div>
  <div class="abs bearings">
    <div class="abs bearings-title heading">Log Down Wheel Bearing Temps</div>
    <div class="abs check" style="left:13px"><span class="box"><svg class="abs" style="left:-1px;top:-6px" width="22" height="20" viewBox="0 0 22 20"><path d="M3 10l5 5L20 2" fill="none" stroke="#1d1d1d" stroke-width="2.4"/></svg></span>Prime Movers</div>
    <div class="abs check" style="left:167px"><span class="box"></span>&nbsp;&nbsp;Trailers</div>

    <div class="abs field bearing" style="left:10px;top:80px">Steer axel FL<span class="line"></span></div>
    <div class="abs field bearing" style="left:180px;top:80px">Steer axel FR<span class="line"></span></div>
    <div class="abs field bearing" style="left:356px;top:80px">1st drive axel L<span class="line"></span></div>
    <div class="abs field bearing" style="left:651px;top:80px">1st axel DS<span class="line"></span></div>
    <div class="abs field bearing" style="left:821px;top:80px">1st axel PS<span class="line"></span></div>
    <div class="abs field bearing" style="left:997px;top:80px">2nd axel DS<span class="line"></span></div>

    <div class="abs field bearing" style="left:10px;top:121px">1st drive axel R<span class="line"></span></div>
    <div class="abs field bearing" style="left:180px;top:121px">2nd drive axel L<span class="line"></span></div>
    <div class="abs field bearing" style="left:356px;top:121px">2nd drive axel R<span class="line"></span></div>
    <div class="abs field bearing" style="left:651px;top:121px">2nd axel PS<span class="line"></span></div>
    <div class="abs field bearing" style="left:821px;top:121px">3rd axel DS<span class="line"></span></div>
    <div class="abs field bearing" style="left:997px;top:121px">3rd axel PS<span class="line"></span></div>
  </div>
</section>

</body>
</html>
```